The Marlowfield Career mentor

The service is premium. It is aimed at people 18-30, so students and those looking to change their first job, principally in the UK but also global. It is offering a very personalised CV writing service and is much more expensive than others on offer. I am very keen that it should look simple and premium. It needs to look very professional, reflecting the aspirational jobs that the clients will be applying for.
If there were three words that summed it up: modern, clean, premium.
I am waiting for all the testimonials to come in but they need to form a major part of the website.
I am also waiting for the full logo design files so that I can upload them. In the meantime there is a copy of the logo.
Thoughts to help those yet to send a design...
This is a premium service and some of the designs have looked very generic. The focus needs to be on quality and the process mentioned in the brief. The partnership and the advantages it brings are crucial but few have mentioned that.

```html
<!DOCTYPE html>
<html lang="en">
<head>
<meta charset="utf-8">
<title>The Marlowfield Career Mentor</title>
<link href="https://fonts.googleapis.com/css2?family=Poppins:wght@400;500;600;700&family=Cinzel:wght@500;600&display=swap" rel="stylesheet">
<style>
:root{
  --blue:#0f67b7;
  --blue-dark:#0b4f93;
  --navy:#1c2f50;
  --ink:#222831;
  --text:#3a3f47;
  --grey:#e4e5e7;
  --white:#ffffff;
  --photo-a:#c9ccc9;
  --photo-b:#8a8f93;
}
*{margin:0;padding:0;box-sizing:border-box}
html,body{width:1200px;height:4535px;overflow:hidden}
body{font-family:"Poppins",sans-serif;color:var(--text);background:var(--white);position:relative}
.abs{position:absolute}
.photo{background:linear-gradient(135deg,var(--photo-a),var(--photo-b))}

/* header */
.site-header{top:0;left:0;width:1200px;height:75px;background:var(--white);z-index:5}
.brand{left:110px;top:20px;display:flex;align-items:center;gap:10px;font-weight:600;font-size:19px;color:var(--blue);letter-spacing:.3px;white-space:nowrap}
.brand-mark{width:30px;height:30px;border:2px solid var(--blue);flex:none}
.nav{left:616px;top:22px;display:flex;gap:38px;font-size:15px;font-weight:500;color:var(--ink)}
.nav .active{color:var(--blue)}
.btn{display:inline-flex;align-items:center;gap:10px;border-radius:24px;font-weight:500;text-transform:uppercase;letter-spacing:.4px}
.btn-primary{background:var(--blue);color:var(--white)}
.header-cta{left:940px;top:12px;height:46px;padding:0 22px;font-size:12px}

/* hero */
.hero{top:75px;left:0;width:1200px;height:700px}
.hero-photo{top:0;left:0;width:1200px;height:650px;clip-path:polygon(0 0,100% 0,100% 85%,50% 100%,0 85%);background:linear-gradient(160deg,#e9eceb 0%,#b8bcbb 45%,#6d6f70 100%)}
.hero-chevron{left:0;top:585px}
.hero-text{top:22px;left:0;width:1200px;text-align:center}
.hero-kicker{font-size:17px;color:var(--ink);letter-spacing:.5px}
.hero-title{font-family:"Cinzel",serif;font-weight:600;font-size:43px;color:var(--ink);letter-spacing:2px;margin-top:6px}
.hero-cta{margin-top:14px;height:42px;padding:0 24px;font-size:12px}
.slider-dots{left:1127px;top:312px;display:flex;flex-direction:column;gap:9px}
.slider-dots span{width:11px;height:11px;border:1.5px solid var(--blue);border-radius:50%;background:var(--white)}
.slider-dots .on{background:var(--blue)}

/* intro */
.intro-frame-top{left:93px;top:818px;width:150px;height:120px;background:var(--blue)}
.intro-frame-bot{left:93px;top:1090px;width:150px;height:105px;background:var(--blue)}
.intro-photo-main{left:110px;top:836px;width:388px;height:340px}
.intro-photo-small{left:382px;top:1050px;width:198px;height:172px;border:3px solid var(--white);background:linear-gradient(135deg,#b4bcc4,#59616b)}
.intro-copy{left:607px;top:847px;width:545px}
.question{font-weight:600;font-size:16.5px;color:var(--ink);margin-bottom:20px}
.intro-copy p.body{font-size:14.5px;line-height:26px;margin-bottom:14px}
.intro-copy .first{margin-top:14px}
.wide-copy{left:117px;width:960px;font-size:15px;line-height:26px}

.benefits{top:1490px;left:128px;display:flex;gap:44px}
.benefit{width:286px;height:268px;background:var(--white);box-shadow:0 4px 14px rgba(0,0,0,.14);border-radius:4px;text-align:center;padding-top:42px}
.benefit svg{width:104px;height:104px}
.benefit h3{font-weight:500;font-size:19px;color:var(--ink);line-height:25px;margin-top:38px}
.benefit:nth-child(3){width:237px}

/* partnership */
.partnership{top:1955px;left:0;width:1200px;height:650px;background:linear-gradient(120deg,#0d63b1,#1670c2 60%,#0b5aa4);clip-path:polygon(0 0,100% 0,100% 83%,50% 100%,0 83%)}
.partnership-copy{left:115px;top:2040px;width:545px;color:var(--white)}
.partnership-copy h2{font-size:39px;font-weight:600;margin-bottom:18px}
.partnership-copy p{font-size:15px;line-height:26px;margin-bottom:12px}
.btn-light{background:var(--white);color:var(--ink);height:44px;padding:0 22px;font-size:12px;margin-top:6px}
.partner-frame{left:712px;top:2053px;width:390px;height:382px;background:var(--white)}
.partner-photo{left:697px;top:2023px;width:390px;height:390px;border:2px solid var(--white);background:linear-gradient(135deg,#c7b8a6,#6d6258)}

/* testimonials */
.testimonials-title{top:2670px;left:0;width:1200px;text-align:center;font-size:39px;font-weight:600;color:var(--navy)}
.quote-card{width:308px;height:335px;background:var(--white);box-shadow:0 4px 14px rgba(0,0,0,.14);border-radius:4px;padding:58px 20px 0;text-align:center}
.quote-card p{font-size:15px;line-height:24.5px;color:var(--text)}
.quote-mark{position:absolute;right:28px;bottom:56px;width:40px;height:34px}
.quote-name{position:absolute;left:10px;right:10px;bottom:10px;height:56px;background:var(--grey);font-size:15px;display:flex;align-items:center;justify-content:center;color:var(--text)}
.quote-card.featured{background:var(--blue);border:3px solid var(--blue-dark);height:328px;padding-top:32px}
.quote-card.featured p{color:var(--white)}
.quote-card.featured .quote-name{background:var(--blue-dark);color:var(--white)}
.view-all{top:3930px;left:535px;height:46px;padding:0 28px;font-size:12px}

/* footer */
.footer-chevron{top:4058px;left:0;width:1200px;height:150px}
.site-footer{top:4200px;left:0;width:1200px;height:335px;background:var(--navy);color:var(--white)}
.footer-brand{left:155px;top:104px;display:flex;align-items:center;gap:12px;font-size:16px;font-weight:500;white-space:nowrap}
.footer-brand .brand-mark{border-color:var(--white);width:32px;height:32px}
.footer-col{top:38px}
.footer-col h4{font-size:17px;font-weight:600;margin-bottom:6px}
.footer-col .rule{width:54px;height:2px;background:var(--blue);margin-bottom:14px}
.footer-col li{list-style:none;font-size:12px;line-height:23px}
.footer-divider{left:110px;top:235px;width:980px;height:1px;background:rgba(255,255,255,.25)}
.copyright{top:257px;left:0;width:1200px;text-align:center;font-size:13px}
</style>
</head>
<body>

<header class="site-header abs">
  <div class="brand abs"><span class="brand-mark"></span>The Marlowfield Career Mentor</div>
  <nav class="nav abs"><span class="active">Home</span><span>About us</span><span>Partnership</span></nav>
  <a class="btn btn-primary header-cta abs">Contact us <span>›</span></a>
</header>

<section class="hero abs">
  <div class="hero-photo abs" role="img" aria-label="Business team meeting around a conference table in a bright office"></div>
  <svg class="hero-chevron abs" width="1200" height="120" viewBox="0 0 1200 120">
    <polygon points="312,101 600,119 888,101 600,106" fill="#0f67b7"/>
  </svg>
  <div class="hero-text abs">
    <div class="hero-kicker">WELCOME TO</div>
    <h1 class="hero-title">MARLOWFIELD CAREER MENTOR</h1>
    <a class="btn btn-primary hero-cta">Get started <span>›</span></a>
  </div>
  <div class="slider-dots abs"><span></span><span class="on"></span><span></span><span></span></div>
</section>

<section class="intro">
  <div class="intro-frame-top abs"></div>
  <div class="intro-frame-bot abs"></div>
  <div class="intro-photo-main abs photo" role="img" aria-label="Colleagues discussing work in a modern office"></div>
  <div class="intro-photo-small abs" role="img" aria-label="Business people reviewing documents together"></div>
  <div class="intro-copy abs">
    <p class="question">Is your current CV not getting you results?</p>
    <p class="question">Do you want to create a CV that stands out from the crowd?</p>
    <p class="question">Do you want to get a job more quickly?</p>
    <p class="question">Do you want to earn more for the job your searching for?</p>
    <p class="body first">If so then invest in a CV writing partnership with Daniel, the career mentor.</p>
    <p class="body">But first read the testimonials. These are real results from real people. They invested in the partnership approach, and they're delighted because it works. The blurb that follows is not as important as what they say – I'd love it if you were the next person to appear in these testimonials.</p>
    <p class="body">People I work with get a job sooner and get a higher paid job.</p>
  </div>
  <p class="wide-copy abs" style="top:1312px">Working with me is personalised, it's a partnership. Together we will build a great CV that will present you in the best way possible, it will increase the chances of you securing the job you want.</p>
  <p class="wide-copy abs" style="top:1388px">And you'll also get this. As a result of my approach everyone I've worked with is better prepared for interview. Our partnership will</p>

  <div class="benefits abs">
    <div class="benefit">
      <svg viewBox="0 0 104 104" fill="none" stroke="#222831" stroke-width="2.5" stroke-linejoin="round">
        <rect x="6" y="66" width="12" height="30"/><rect x="24" y="52" width="12" height="44"/><rect x="42" y="38" width="12" height="58"/><rect x="60" y="22" width="12" height="74"/>
        <path d="M8 92 C40 86 70 70 94 48"/><path d="M82 46 L96 46 L92 60"/>
      </svg>
      <h3>Increase self<br>awareness</h3>
    </div>
    <div class="benefit">
      <svg viewBox="0 0 104 104" fill="none" stroke="#222831" stroke-width="2.5" stroke-linecap="round">
        <path d="M52 24 a24 24 0 0 1 14 43 v10 h-28 v-10 a24 24 0 0 1 14 -43 z"/>
        <path d="M40 84 h24 M43 90 h18"/><path d="M52 40 v20 M42 50 h20"/>
        <g stroke="#0f67b7"><path d="M52 6 v10 M20 20 l7 7 M84 20 l-7 7 M8 50 h10 M86 50 h10 M18 80 l7 -6 M86 80 l-7 -6"/></g>
      </svg>
      <h3>Improve presentation<br>skills</h3>
    </div>
    <div class="benefit">
      <svg viewBox="0 0 104 104" fill="none" stroke="#222831" stroke-width="2.5" stroke-linejoin="round">
        <path d="M52 6 l20 8 v16 c0 14 -10 22 -20 26 c-10 -4 -20 -12 -20 -26 v-16 z"/>
        <path d="M43 31 l7 7 l12 -13" stroke="#0f67b7"/>
        <path d="M6 60 l16 -8 l18 20 l-14 12 z M98 60 l-16 -8 l-18 20 l14 12 z"/>
        <path d="M36 68 l12 12 M44 64 l14 14 M52 62 l12 12"/>
      </svg>
      <h3>Build the right sort<br>of confidence</h3>
    </div>
  </div>
  <p class="wide-copy abs" style="top:1800px">And as a result you'll impress at interview. You'll develop a language and way of expressing yourself that shows the very best of you. And as that language sinks in and becomes part of you, you project a genuine confidence, quietly powerful, that recruiters will want in their teams.</p>
</section>

<section class="partnership abs"></section>
<div class="partnership-copy abs">
  <h2>The Partnership</h2>
  <p>The key to all this success is the partnership. Over four sessions we will, together, build a CV. You will get me, no one else, working with you for four sessions. There is a formula for success but it's not formulaic. Your CV will be personal, you will shine through. Your CV will be elevated above the crowd.</p>
  <p>I offer a premium service, very different to other offerings - so if like those in the testimonials, you get that job sooner, get a higher paid job, the investment is a wise one.</p>
  <p>So take the first step to the best CV you can have.</p>
  <a class="btn btn-light">Contact me now <span>›</span></a>
</div>
<div class="partner-frame abs"></div>
<div class="partner-photo abs" role="img" aria-label="Young professionals collaborating around a laptop"></div>

<h2 class="testimonials-title abs">Testimonials</h2>

<div class="quote-card abs" style="left:112px;top:2805px"><p>"Perspiciatis unde omnis iste natus error sit voluptatem accusantium doloremque laudantium, totam rem aperiam, eaque ipsa quae ab illo inventore veritatis et quasi architecto beatae vitae dictant quia."</p><svg class="quote-mark" viewBox="0 0 40 34"><path fill="#0f67b7" d="M2 34 V18 C2 8 8 2 17 0 L18 5 C12 7 10 11 10 16 H17 V34 Z M22 34 V18 C22 8 28 2 37 0 L38 5 C32 7 30 11 30 16 H37 V34 Z"/></svg><div class="quote-name">– Elena Hartwell, CEA</div></div>
<div class="quote-card featured abs" style="left:446px;top:2745px"><p>"Perspiciatis unde omnis iste natus error sit voluptatem accusantium doloremque laudantium, totam rem aperiam, eaque ipsa quae ab illo inventore veritatis et quasi architecto beatae vitae dicta sunt explicabo.</p><svg class="quote-mark" viewBox="0 0 40 34"><path fill="#fff" d="M2 34 V18 C2 8 8 2 17 0 L18 5 C12 7 10 11 10 16 H17 V34 Z M22 34 V18 C22 8 28 2 37 0 L38 5 C32 7 30 11 30 16 H37 V34 Z"/></svg><div class="quote-name">– Tobias Whitcombe, CEO</div></div>
<div class="quote-card abs" style="left:780px;top:2805px"><p>"Perspiciatis unde omnis iste natus error sit voluptatem accusantium doloremque laudantium, totam rem aperiam, eaque ipsa quae ab illo inventore veritatis et quasi architecto beatae vitae dictant quia."</p><svg class="quote-mark" viewBox="0 0 40 34"><path fill="#0f67b7" d="M2 34 V18 C2 8 8 2 17 0 L18 5 C12 7 10 11 10 16 H17 V34 Z M22 34 V18 C22 8 28 2 37 0 L38 5 C32 7 30 11 30 16 H37 V34 Z"/></svg><div class="quote-name">– Elena Hartwell, CEA</div></div>

<div class="quote-card abs" style="left:112px;top:3180px"><p>"Perspiciatis unde omnis iste natus error sit voluptatem accusantium doloremque laudantium, totam rem aperiam, eaque ipsa quae ab illo inventore veritatis et quasi architecto beatae vitae dictant quia."</p><svg class="quote-mark" viewBox="0 0 40 34"><path fill="#0f67b7" d="M2 34 V18 C2 8 8 2 17 0 L18 5 C12 7 10 11 10 16 H17 V34 Z M22 34 V18 C22 8 28 2 37 0 L38 5 C32 7 30 11 30 16 H37 V34 Z"/></svg><div class="quote-name">– Elena Hartwell, CEA</div></div>
<div class="quote-card abs" style="left:446px;top:3180px"><p>"Perspiciatis unde omnis iste natus error sit voluptatem accusantium doloremque laudantium, totam rem aperiam, eaque ipsa quae ab illo inventore veritatis et quasi architecto beatae vitae dictant quia."</p><svg class="quote-mark" viewBox="0 0 40 34"><path fill="#0f67b7" d="M2 34 V18 C2 8 8 2 17 0 L18 5 C12 7 10 11 10 16 H17 V34 Z M22 34 V18 C22 8 28 2 37 0 L38 5 C32 7 30 11 30 16 H37 V34 Z"/></svg><div class="quote-name">– Elena Hartwell, CEA</div></div>
<div class="quote-card abs" style="left:780px;top:3180px"><p>"Perspiciatis unde omnis iste natus error sit voluptatem accusantium doloremque laudantium, totam rem aperiam, eaque ipsa quae ab illo inventore veritatis et quasi architecto beatae vitae dictant quia."</p><svg class="quote-mark" viewBox="0 0 40 34"><path fill="#0f67b7" d="M2 34 V18 C2 8 8 2 17 0 L18 5 C12 7 10 11 10 16 H17 V34 Z M22 34 V18 C22 8 28 2 37 0 L38 5 C32 7 30 11 30 16 H37 V34 Z"/></svg><div class="quote-name">– Elena Hartwell, CEA</div></div>

<div class="quote-card abs" style="left:112px;top:3555px"><p>"Perspiciatis unde omnis iste natus error sit voluptatem accusantium doloremque laudantium, totam rem aperiam, eaque ipsa quae ab illo inventore veritatis et quasi architecto beatae vitae dictant quia."</p><svg class="quote-mark" viewBox="0 0 40 34"><path fill="#0f67b7" d="M2 34 V18 C2 8 8 2 17 0 L18 5 C12 7 10 11 10 16 H17 V34 Z M22 34 V18 C22 8 28 2 37 0 L38 5 C32 7 30 11 30 16 H37 V34 Z"/></svg><div class="quote-name">– Elena Hartwell, CEA</div></div>
<div class="quote-card abs" style="left:446px;top:3555px"><p>"Perspiciatis unde omnis iste natus error sit voluptatem accusantium doloremque laudantium, totam rem aperiam, eaque ipsa quae ab illo inventore veritatis et quasi architecto beatae vitae dictant quia."</p><svg class="quote-mark" viewBox="0 0 40 34"><path fill="#0f67b7" d="M2 34 V18 C2 8 8 2 17 0 L18 5 C12 7 10 11 10 16 H17 V34 Z M22 34 V18 C22 8 28 2 37 0 L38 5 C32 7 30 11 30 16 H37 V34 Z"/></svg><div class="quote-name">– Elena Hartwell, CEA</div></div>
<div class="quote-card abs" style="left:780px;top:3555px"><p>"Perspiciatis unde omnis iste natus error sit voluptatem accusantium doloremque laudantium, totam rem aperiam, eaque ipsa quae ab illo inventore veritatis et quasi architecto beatae vitae dictant quia."</p><svg class="quote-mark" viewBox="0 0 40 34"><path fill="#0f67b7" d="M2 34 V18 C2 8 8 2 17 0 L18 5 C12 7 10 11 10 16 H17 V34 Z M22 34 V18 C22 8 28 2 37 0 L38 5 C32 7 30 11 30 16 H37 V34 Z"/></svg><div class="quote-name">– Elena Hartwell, CEA</div></div>

<a class="btn btn-primary view-all abs">View all <span>›</span></a>

<svg class="footer-chevron abs" viewBox="0 0 1200 150">
  <polygon points="312,62 600,0 888,62 600,16" fill="#0f67b7"/>
  <polygon points="0,142 600,30 1200,142 1200,150 0,150" fill="#1c2f50"/>
</svg>
<footer class="site-footer abs">
  <div class="footer-brand abs"><span class="brand-mark"></span>The Marlowfield Career Mentor</div>
  <div class="footer-col abs" style="left:507px"><h4>Quick Links</h4><div class="rule"></div><ul><li>Home</li><li>About us</li><li>Partnership</li><li>Contact Us</li></ul></div>
  <div class="footer-col abs" style="left:700px"><h4>Links</h4><div class="rule"></div><ul><li>Copyright</li><li>Terms of Use</li><li>Privacy Policy</li><li>Accessibility</li><li>Sitemap</li></ul></div>
  <div class="footer-col abs" style="left:878px"><h4>Support</h4><div class="rule"></div><ul><li>Team</li><li>About Us</li><li>Careers</li><li>Our Values</li><li>Data Security</li></ul></div>
  <div class="footer-divider abs"></div>
  <p class="copyright abs">©2024. All rights reserved.</p>
</footer>

</body>
</html>
```